Sleek and elegant promotional banner/sign for The Vellinor Law Firm

We need a design for promotional items like banners, signs, print ads, etc. that includes our firm name - "The Vellinor Law Firm" - and what we do. We advise businesses and individuals on legal matters; we represent individuals and businesses in litigation and transactions; we select and create business entities; we solve legal problems for individuals and businesses, etc. PLEASE DO NOT SIMPLY REPEAT THE PREVIOUS SENTENCE ON THE DESIGN. Please create a tag-line or brief description from ours. We need something that describes what we do in concise and creative manner while communicating trust and confidence. The banner must also include our basic contact information: 948.512-7740 (telephone) and vellinorlaw.com (website). You may use one or more of the attached images, but needn't use any with the right design. The design should be sleek and modern.

Target Market(s)

wealthy individuals and small business owners, entrepreneurs

Industry/Entity Type

Lawyer

Font styles to use
Sans Serif

Colors
33a6d7
0556a4
33b8a4

Requirements
Must have
• Firm name, contact information, BRIEF description of our services, sleek and elegant.
• Also, the design must be horizontal - not vertical.
Nice to have
• I'd like to use one of the images
Should not have
• Cliches

```html
<!DOCTYPE html>
<html lang="en">
<head>
<meta charset="utf-8">
<title>The Vellinor Law Firm – Banner</title>
<link rel="stylesheet" href="https://fonts.googleapis.com/css2?family=Open+Sans:wght@600;700&family=Roboto+Condensed:wght@400;700&display=swap">
<style>
  :root {
    --page-bg: #a6a6a6;
    --blue-deep: #0556a4;
    --blue-mid: #1677cf;
    --blue-sky: #33a6d7;
    --puzzle-light: #8fbde3;
    --puzzle-mid: #5f9fd6;
    --puzzle-deep: #3f84c6;
    --teal: #33b8a4;
    --teal-text: #2eae98;
    --white: #ffffff;
  }
  html, body {
    margin: 0;
    width: 1200px;
    height: 1200px;
    overflow: hidden;
    background: var(--page-bg);
  }
  .banner {
    position: absolute;
    left: 109px;
    top: 405px;
    width: 984px;
    height: 393px;
    overflow: hidden;
    background: radial-gradient(ellipse at 25% 35%, #1a8be0 0%, var(--blue-mid) 35%, var(--blue-deep) 100%);
  }
  .banner-art {
    position: absolute;
    inset: 0;
  }
  .firm-name {
    position: absolute;
    left: 0;
    width: 476px;
    top: 41px;
    margin: 0;
    text-align: center;
    font-family: "Open Sans", sans-serif;
    font-weight: 700;
    font-size: 52px;
    line-height: 1;
    color: var(--white);
    letter-spacing: 0.3px;
    white-space: nowrap;
  }
  .firm-subtitle {
    position: absolute;
    left: 0;
    width: 476px;
    top: 97px;
    text-align: center;
    font-family: "Open Sans", sans-serif;
    font-weight: 600;
    font-size: 30px;
    line-height: 1;
    color: var(--white);
  }
  .tagline {
    position: absolute;
    left: 0;
    top: 0;
    width: 476px;
    height: 333px;
    margin: 0;
    font-family: "Roboto Condensed", sans-serif;
    color: var(--white);
    line-height: 1;
  }
  .tagline span {
    position: absolute;
    left: 0;
    width: 476px;
    text-align: center;
    white-space: nowrap;
  }
  .tagline-lead {
    top: 149px;
    font-weight: 700;
    font-size: 88px;
  }
  .tagline-mid {
    top: 226px;
    font-weight: 400;
    font-size: 44px;
  }
  .tagline-end {
    top: 265px;
    font-weight: 400;
    font-size: 51px;
  }
  .website {
    position: absolute;
    left: 52px;
    top: 340px;
    font-family: "Open Sans", sans-serif;
    font-weight: 700;
    font-size: 35px;
    line-height: 1;
    color: var(--teal-text);
    white-space: nowrap;
  }
  .phone {
    position: absolute;
    left: 518px;
    top: 325px;
    display: flex;
    align-items: center;
    gap: 16px;
    font-family: "Open Sans", sans-serif;
    font-weight: 700;
    font-size: 59px;
    line-height: 1;
    color: var(--white);
    white-space: nowrap;
  }
</style>
</head>
<body>
  <section class="banner">
    <svg class="banner-art" width="984" height="393" viewBox="0 0 984 393" aria-hidden="true">
      <defs>
        <radialGradient id="puzzleTone" cx="0.58" cy="0.56" r="0.75">
          <stop offset="0" stop-color="var(--puzzle-light)"/>
          <stop offset="0.45" stop-color="var(--puzzle-mid)"/>
          <stop offset="1" stop-color="var(--puzzle-deep)"/>
        </radialGradient>
        <linearGradient id="puzzleFade" x1="0" y1="0" x2="1" y2="0">
          <stop offset="0" stop-color="#fff" stop-opacity="0"/>
          <stop offset="0.28" stop-color="#fff" stop-opacity="1"/>
          <stop offset="1" stop-color="#fff" stop-opacity="1"/>
        </linearGradient>
        <mask id="puzzleMask">
          <rect x="380" y="0" width="604" height="333" fill="url(#puzzleFade)"/>
        </mask>
      </defs>
      <g role="img" aria-label="Photo of a blue jigsaw puzzle arranged in concentric rings" mask="url(#puzzleMask)">
        <rect x="380" y="0" width="604" height="333" fill="url(#puzzleTone)"/>
      </g>
      <path class="wave" d="M0 305 C220 330 420 300 600 240 C760 185 880 160 984 165 L984 205 C860 200 740 240 600 285 C430 335 220 345 0 325 Z" fill="#ffffff" opacity="0.18"/>
      <path class="wave" d="M120 330 C320 300 520 240 700 200 C820 175 920 170 984 180 L984 190 C900 185 800 200 690 230 C520 280 330 320 120 330 Z" fill="#ffffff" opacity="0.3"/>
      <path class="wave" d="M0 340 C200 320 420 330 620 300 C800 270 900 250 984 255 L984 333 L0 333 Z" fill="#0a5fae" opacity="0.35"/>
      <line x1="24" y1="112" x2="161" y2="112" stroke="var(--teal)" stroke-width="3"/>
      <line x1="324" y1="112" x2="451" y2="112" stroke="var(--teal)" stroke-width="3"/>
      <polygon class="web-strip" points="0,333 491,333 470,393 0,393" fill="#ffffff"/>
      <polygon class="phone-strip" points="509,313 984,313 984,393 488,393" fill="var(--teal)"/>
    </svg>

    <h1 class="firm-name">THE VELLINOR</h1>
    <div class="firm-subtitle">LAW FIRM</div>

    <p class="tagline">
      <span class="tagline-lead">WE SOLVE</span>
      <span class="tagline-mid">THE MOST PUZZLING</span>
      <span class="tagline-end">LEGAL PROBLEMS</span>
    </p>

    <div class="website">www.vellinorlaw.com</div>

    <div class="phone">
      <svg width="50" height="50" viewBox="0 0 50 50" aria-hidden="true">
        <circle cx="25" cy="25" r="22" fill="none" stroke="#fff" stroke-width="3"/>
        <path d="M17 15 l5 -1 l3 7 l-3 2 c1.5 3 3.5 5 6.5 6.5 l2 -3 l7 3 l-1 5 c-11 1 -20 -8 -19.5 -19.5z" fill="#fff"/>
        <path d="M28 14 a9 9 0 0 1 8 8" fill="none" stroke="#fff" stroke-width="2.2"/>
        <path d="M28 19 a4 4 0 0 1 3.5 3.5" fill="none" stroke="#fff" stroke-width="2.2"/>
      </svg>
      <span>948.512-7740</span>
    </div>
  </section>
</body>
</html>
```